Awesome Design for a Quietmind Therapy

We need a simple but modern design for a Quietmind Therapy which opened recently. A logo, letterhead and a business card. Maybe something with the greek letter psi.

Font styles to use
Serif
Sans Serif

```html
<!DOCTYPE html>
<html lang="en">
<head>
<meta charset="utf-8">
<title>Quietmind Therapy – Stationery</title>
<link href="https://fonts.googleapis.com/css2?family=Questrial&family=Nunito:wght@700&display=swap" rel="stylesheet">
<style>
  :root{
    --backdrop:#bcbdc0;
    --ink:#171717;
    --brand-blue:#168dca;
    --paper:#ffffff;
    --shadow:rgba(0,0,0,.45);
  }
  *{margin:0;padding:0;box-sizing:border-box}
  html,body{width:1077px;height:1200px;overflow:hidden}
  body{background:var(--backdrop);position:relative;font-family:"Questrial",sans-serif}

  /* Letterhead */
  .letterhead{position:absolute;left:235px;top:182px;width:639px;height:827px;background:var(--paper);box-shadow:5px 5px 6px var(--shadow)}
  .letterhead-header{position:absolute;left:0;top:0;width:639px;height:111px}
  .letterhead-footer{position:absolute;left:0;bottom:0;width:639px;height:111px}
  .brand{position:absolute;display:flex;align-items:center;color:var(--brand-blue);font-family:"Questrial",sans-serif;font-weight:400}
  .brand-dot{border-radius:50%;background:var(--brand-blue);flex:none}
  .brand-name{line-height:1;letter-spacing:.04em}
  .letterhead .brand{left:128px;top:24px;gap:12px}
  .letterhead .brand-dot{width:40px;height:40px}
  .letterhead .brand-name{font-size:30px}
  .letterhead .brand-name span{display:block}

  .footer-item{position:absolute;display:flex;align-items:flex-start;color:var(--paper);font-size:14px;line-height:16px;letter-spacing:.02em}
  .footer-item svg{position:absolute;fill:var(--paper)}
  .footer-item .label{position:absolute;white-space:nowrap}

  /* Business card */
  .business-card{position:absolute;left:162px;top:534px;width:263px;height:151px;background:var(--ink);box-shadow:5px 5px 6px var(--shadow);overflow:hidden}
  .business-card .brand{left:45px;top:22px;gap:7px}
  .business-card .brand-dot{width:22px;height:22px}
  .business-card .brand-name{font-size:15px}
  .business-card .brand-name span{display:block}
  .card-stripe{position:absolute;left:0;width:263px;background:var(--brand-blue)}
  .card-stripe.top{top:83px;height:4px}
  .card-stripe.bottom{top:146px;height:5px}
  .card-divider{position:absolute;background:var(--paper)}
  .card-contact-panel{position:absolute;left:106px;top:88px;width:157px;height:57px;background:var(--brand-blue)}
  .card-holder{position:absolute;right:172px;top:102px;text-align:right;color:var(--paper)}
  .card-holder .name{font-family:"Nunito",sans-serif;font-weight:700;font-size:13px;line-height:13px}
  .card-holder .role{font-size:9.5px;line-height:11px}
  .card-contact{position:absolute;left:136px;color:var(--paper);font-size:6px;line-height:7px;white-space:nowrap}
  .card-icon{position:absolute;left:124px;fill:var(--paper)}
</style>
</head>
<body>

<section class="letterhead">
  <svg class="letterhead-header" viewBox="0 0 639 111" aria-hidden="true">
    <path d="M0 0H639A111 111 0 0 1 528 111H0Z" fill="var(--ink)"/>
  </svg>
  <div class="brand">
    <div class="brand-dot"></div>
    <div class="brand-name"><span>QUIETMIND</span><span>THERAPY</span></div>
  </div>

  <svg class="letterhead-footer" viewBox="0 0 639 111" aria-hidden="true">
    <path d="M0 111A111 111 0 0 1 111 0H639V111Z" fill="var(--brand-blue)"/>
  </svg>

  <div class="footer-item" style="left:54px;top:745px">
    <svg width="20" height="20" viewBox="0 0 24 24" style="left:0;top:0"><path d="M6.6 10.8a15.1 15.1 0 0 0 6.6 6.6l2.2-2.2a1 1 0 0 1 1-.25 11.4 11.4 0 0 0 3.6.6 1 1 0 0 1 1 1V20a1 1 0 0 1-1 1A17 17 0 0 1 3 4a1 1 0 0 1 1-1h3.5a1 1 0 0 1 1 1c0 1.25.2 2.45.6 3.6a1 1 0 0 1-.25 1z"/></svg>
    <span class="label" style="left:35px;top:4px">(+44)7000 123456</span>
  </div>
  <div class="footer-item" style="left:54px;top:782px">
    <svg width="22" height="16" viewBox="0 0 22 16" style="left:0;top:0"><path d="M0 0h22v16H0zM2 2v.4l9 6.8 9-6.8V2zm0 2.9V14h5.5zM20 14V4.9L14.5 14zM9 10.4 3.3 14h15.4L13 10.4l-2 1.5z"/></svg>
    <span class="label" style="left:35px;top:0">hello@quietmindtherapy.com</span>
  </div>
  <div class="footer-item" style="left:360px;top:742px">
    <svg width="22" height="22" viewBox="0 0 24 24" style="left:0;top:0"><path d="M12 1a11 11 0 1 0 0 22 11 11 0 0 0 0-22zm0 2c1.2 1.3 2.1 3 2.5 5h-5c.4-2 1.3-3.7 2.5-5zM9.3 3.5C8.6 4.8 8 6.3 7.6 8H4.3a9 9 0 0 1 5-4.5zm5.4 0a9 9 0 0 1 5 4.5h-3.3c-.4-1.7-1-3.2-1.7-4.5zM3.6 10h3.7a16 16 0 0 0 0 4H3.6a9 9 0 0 1 0-4zm5.7 0h5.4a14 14 0 0 1 0 4H9.3a14 14 0 0 1 0-4zm7.4 0h3.7a9 9 0 0 1 0 4h-3.7a16 16 0 0 0 0-4zM4.3 16h3.3c.4 1.7 1 3.2 1.7 4.5a9 9 0 0 1-5-4.5zm5.2 0h5c-.4 2-1.3 3.7-2.5 5-1.2-1.3-2.1-3-2.5-5zm6.9 0h3.3a9 9 0 0 1-5 4.5c.7-1.3 1.3-2.8 1.7-4.5z"/></svg>
    <span class="label" style="left:35px;top:2px">www.quietmindtherapy.com</span>
  </div>
  <div class="footer-item" style="left:361px;top:772px">
    <svg width="20" height="30" viewBox="0 0 20 30" style="left:0;top:0"><path d="M10 0A10 10 0 0 0 0 10c0 7 10 20 10 20s10-13 10-20A10 10 0 0 0 10 0zm0 6.5a3.5 3.5 0 1 1 0 7 3.5 3.5 0 0 1 0-7z"/></svg>
    <span class="label" style="left:34px;top:0">12 Harbour Lane<br>Fairview, VA 20000</span>
  </div>
</section>

<section class="business-card">
  <div class="brand">
    <div class="brand-dot"></div>
    <div class="brand-name"><span>QUIETMIND</span><span>THERAPY</span></div>
  </div>
  <div class="card-stripe top"></div>
  <div class="card-divider" style="left:105px;top:87px;width:1px;height:59px"></div>
  <div class="card-contact-panel"></div>
  <div class="card-divider" style="left:0;top:145px;width:263px;height:1px"></div>
  <div class="card-stripe bottom"></div>

  <div class="card-holder">
    <div class="name">Your Name</div>
    <div class="role">President</div>
  </div>

  <svg class="card-icon" style="top:91px" width="8" height="8" viewBox="0 0 24 24"><path d="M6.6 10.8a15.1 15.1 0 0 0 6.6 6.6l2.2-2.2a1 1 0 0 1 1-.25 11.4 11.4 0 0 0 3.6.6 1 1 0 0 1 1 1V20a1 1 0 0 1-1 1A17 17 0 0 1 3 4a1 1 0 0 1 1-1h3.5a1 1 0 0 1 1 1c0 1.25.2 2.45.6 3.6a1 1 0 0 1-.25 1z"/></svg>
  <span class="card-contact" style="top:92px">(+44)7000 123456</span>
  <svg class="card-icon" style="top:104px" width="9" height="6" viewBox="0 0 22 16"><path d="M0 0h22v16H0zM2 2v.4l9 6.8 9-6.8V2zm0 2.9V14h5.5zM20 14V4.9L14.5 14zM9 10.4 3.3 14h15.4L13 10.4l-2 1.5z"/></svg>
  <span class="card-contact" style="top:103px">hello@quietmindtherapy.com</span>
  <svg class="card-icon" style="top:115px" width="9" height="9" viewBox="0 0 24 24"><path d="M12 1a11 11 0 1 0 0 22 11 11 0 0 0 0-22zm-8.4 9h16.8a9 9 0 0 1 0 4H3.6a9 9 0 0 1 0-4zM12 3c1.6 2 2.5 5.5 2.5 9s-.9 7-2.5 9c-1.6-2-2.5-5.5-2.5-9S10.4 5 12 3z"/></svg>
  <span class="card-contact" style="top:115px">www.quietmindtherapy.com</span>
  <svg class="card-icon" style="top:127px" width="8" height="12" viewBox="0 0 20 30"><path d="M10 0A10 10 0 0 0 0 10c0 7 10 20 10 20s10-13 10-20A10 10 0 0 0 10 0zm0 6.5a3.5 3.5 0 1 1 0 7 3.5 3.5 0 0 1 0-7z"/></svg>
  <span class="card-contact" style="top:127px">12 Harbour Lane<br>Fairview, VA 20000</span>
</section>

</body>
</html>
```